Loan Company looking to offer special summer loan rate for closed customers

We are wanting to design an A5 Summer Holiday themed leaflet. We would like to offer a 10% Cashback when re-opening their loan account.
The leaflet is aimed at our closed customers. We would like to use bright summer colours. I have uploaded one of our Christmas promotion leaflets for you to include the highlighted information to use in this new project. We have also uploaded some ideas of examples that we have seen online as rough guide.
"10% Cashback on all re-opened accounts in July and August 2023!"

```html
<!DOCTYPE html>
<html lang="en">
<head>
<meta charset="utf-8">
<title>Summer Cashback Leaflet</title>
<link rel="stylesheet" href="https://fonts.googleapis.com/css2?family=Bebas+Neue&family=Montserrat:wght@400;600&display=swap">
<style>
  :root {
    --backdrop: #c8c8ca;
    --deep-teal: #0b6378;
    --sea: #1aa9c4;
    --sky-light: #bfe9f2;
    --haze: #f4fbfd;
    --sand: #f2d7a8;
    --sand-light: #f8e6c6;
    --leaf: #4f8a6a;
    --leaf-dark: #2f5f4a;
    --pill-top: #7faf86;
    --pill-bottom: #35604a;
    --frame: #2f5f55;
    --ink: #161616;
    --white: #ffffff;
    --umbrella: #f5a33a;
  }
  * { box-sizing: border-box; margin: 0; padding: 0; }
  html, body { width: 917px; height: 1200px; overflow: hidden; }
  body { background: var(--backdrop); position: relative; font-family: "Montserrat", sans-serif; }

  .leaflet {
    position: absolute; left: 70px; top: 0; width: 777px; height: 1200px;
    overflow: hidden;
  }
  .beach-scene {
    position: absolute; inset: 0;
    background: linear-gradient(180deg,
      var(--deep-teal) 0%, var(--sea) 22%, var(--sky-light) 45%, var(--haze) 58%,
      var(--haze) 62%, var(--sea) 66%, #7fd3e0 70%, var(--sand-light) 74%,
      var(--sand) 88%, #cfeef5 93%, var(--sea) 96%, var(--deep-teal) 100%);
  }
  .art { position: absolute; border-radius: 40%; }
  .art-palm-left { left: -40px; top: -40px; width: 240px; height: 330px; background: radial-gradient(ellipse at 30% 30%, var(--leaf) 0%, rgba(79,138,106,0.55) 55%, rgba(79,138,106,0) 75%); }
  .art-palm-right { right: -40px; top: -40px; width: 240px; height: 330px; background: radial-gradient(ellipse at 70% 30%, var(--leaf) 0%, rgba(79,138,106,0.55) 55%, rgba(79,138,106,0) 75%); }
  .art-plants { left: -40px; top: 680px; width: 290px; height: 310px; background: radial-gradient(ellipse at 30% 50%, var(--leaf-dark) 0%, rgba(79,138,106,0.6) 55%, rgba(79,138,106,0) 75%); }
  .art-umbrella-chair { left: 590px; top: 510px; width: 230px; height: 390px; border-radius: 30%; background: radial-gradient(ellipse at 60% 30%, rgba(245,163,58,0.85) 0%, rgba(245,163,58,0.45) 45%, rgba(245,163,58,0) 72%); }
  .art-shell { left: 640px; top: 925px; width: 60px; height: 60px; border-radius: 50%; background: #f2b8a4; }

  .brand { position: absolute; top: 60px; left: 0; right: 0; text-align: center; color: var(--white); }
  .brand-name { font-weight: 600; font-size: 52px; line-height: 1; letter-spacing: 0.5px; }
  .brand-sub { font-weight: 600; font-size: 14px; margin-top: 8px; }

  .offer-frame {
    position: absolute; left: 147px; top: 270px; width: 483px; height: 225px;
    border: 1.5px solid var(--frame); border-radius: 14px;
  }
  .offer-headline {
    position: absolute; left: 0; right: 0; top: 272px; text-align: center;
    font-family: "Bebas Neue", sans-serif; font-size: 96px; line-height: 1; color: var(--white);
    text-shadow: 0 3px 6px rgba(0,0,0,0.35);
  }
  .offer-pill {
    position: absolute; left: 110px; top: 369px; width: 558px; height: 63px;
    border-radius: 32px; background: linear-gradient(180deg, var(--pill-top), var(--pill-bottom));
    display: flex; align-items: center; justify-content: center;
    font-family: "Bebas Neue", sans-serif; font-size: 55px; color: var(--white); padding-top: 4px;
  }
  .offer-dates {
    position: absolute; left: 0; right: 0; top: 438px; text-align: center;
    font-family: "Bebas Neue", sans-serif; font-size: 46px; color: var(--ink);
  }

  .rep-example {
    position: absolute; left: 159px; top: 590px; width: 460px;
    font-size: 15.5px; line-height: 1.4; color: var(--ink); text-align: justify; text-align-last: center;
  }
  .rep-example p + p { margin-top: 20px; }

  .terms { position: absolute; left: 0; right: 0; top: 926px; text-align: center; font-size: 14.5px; line-height: 1.35; color: var(--ink); }
  .terms strong { font-weight: 600; }

  .contact { position: absolute; left: 0; right: 0; top: 1016px; text-align: center; font-family: "Bebas Neue", sans-serif; color: var(--ink); }
  .contact-lead { font-size: 34px; line-height: 1; }
  .contact-sub { font-size: 26px; line-height: 1; margin-top: 2px; }
  .contact-phone { font-size: 82px; line-height: 1; color: var(--white); margin-top: 12px; letter-spacing: 1px; }
</style>
</head>
<body>
  <main class="leaflet">
    <div class="beach-scene" role="img" aria-label="Sunny beach background with sky, sea and sand"></div>
    <div class="art art-palm-left" role="img" aria-label="Palm leaves in the top left corner"></div>
    <div class="art art-palm-right" role="img" aria-label="Palm leaves in the top right corner"></div>
    <div class="art art-plants" role="img" aria-label="Tropical plants on the left of the beach"></div>
    <div class="art art-umbrella-chair" role="img" aria-label="Orange beach umbrella and striped deck chair"></div>
    <div class="art art-shell" role="img" aria-label="Seashell on the sand"></div>

    <header class="brand">
      <div class="brand-name">Harbour</div>
      <div class="brand-sub">Lending Services (Northshire) Limited</div>
    </header>

    <div class="offer-frame"></div>
    <h1 class="offer-headline">10% Cashback</h1>
    <div class="offer-pill">On all re-opened accounts</div>
    <div class="offer-dates">In July and August 2023!</div>

    <section class="rep-example">
      <p>Representative example: Loan amount $150.00 payable over 23 weeks at $10.50 per week.</p>
      <p>interest is $91.50 The Total amount payable is $241.50. Interest rate is 138.29% per annum (fixed). 838.39% APR representative.</p>
    </section>

    <section class="terms">
      <strong>Term and Conditions apply.</strong><br>
      All credit is Subject to status &amp; affordability.<br>
      Written quotations on request
    </section>

    <footer class="contact">
      <div class="contact-lead">For more information</div>
      <div class="contact-sub">Contact our office on</div>
      <div class="contact-phone">01632 960 418</div>
    </footer>
  </main>
</body>
</html>
```